Flyer Advertisement Simple But Creative

Flyer dimensions 4" x 6"

Simple design with logo and additional info. On the front of the flyer:

- place the logo at the top
- beneath the logo add the website and phone number
- simple less is more approach
- feel free to add your own personal touch

On the back:

- Requirements
- Perfect for Birthdays and Anniversaries
- Rentals available hourly, daily, and weekly
- Group Rentals available at discounted rates
- Enter to win a free rental - url and QR code

Industry/Entity Type

Car Rental

Font styles to use
Serif
Sans Serif

Colors

Designer to choose colors to be used in the design.

Requirements
Must have
• FRONT:
• Please include our phone number and website:
• 832-519-2086
• www.BrazosTrikeHire.com
• BACK:
• REQUIREMENTS
• At least 25 years of age
• Valid Driver's License
• Debit or Credit Card
• Must know how to drive a manual transmission or stick shift

```html
<!DOCTYPE html>
<html lang="en">
<head>
<meta charset="UTF-8">
<title>Trike Rental Flyer – Requirements</title>
<link rel="stylesheet" href="https://fonts.googleapis.com/css2?family=Russo+One&family=Itim&display=swap">
<style>
  :root {
    --title-red: #d0121a;
    --band-red: #c20a0f;
    --band-black: #0d0d0d;
    --text-dark: #1a1a1a;
    --text-light: #ffffff;
    --panel: rgba(255, 255, 255, 0.38);
    --vehicle-tone: #3b2f2a;
  }
  html, body {
    margin: 0;
    padding: 0;
    overflow: hidden;
    background: #ffffff;
  }
  .flyer {
    position: relative;
    width: 800px;
    height: 1200px;
    overflow: hidden;
  }
  .backdrop-photo {
    position: absolute;
    inset: 0;
    width: 800px;
    height: 1200px;
  }
  .vehicle-photo {
    position: absolute;
    left: 46px;
    top: 530px;
    width: 616px;
    height: 292px;
  }
  .title {
    position: absolute;
    left: 88px;
    top: 160px;
    margin: 0;
    font-family: "Russo One", sans-serif;
    font-size: 58px;
    letter-spacing: 2px;
    color: var(--title-red);
    transform: skewX(-14deg) scaleX(1.2) scaleY(0.9);
    transform-origin: left bottom;
    line-height: 1;
    white-space: nowrap;
  }
  .highlights {
    position: absolute;
    left: 76px;
    top: 220px;
    width: 644px;
    height: 196px;
    margin: 0;
    padding: 10px 0 0 5px;
    box-sizing: border-box;
    list-style: none;
    background: var(--panel);
    font-family: "Itim", sans-serif;
    font-size: 28px;
    color: var(--text-dark);
    white-space: nowrap;
  }
  .highlights li {
    height: 42.5px;
    line-height: 42.5px;
  }
  .bottom-band {
    position: absolute;
    left: 0;
    top: 900px;
    width: 800px;
    height: 300px;
  }
  .requirements {
    position: absolute;
    right: 13px;
    top: 1012px;
    margin: 0;
    padding: 0;
    list-style: none;
    text-align: right;
    font-family: "Itim", sans-serif;
    font-size: 28px;
    color: var(--text-light);
    white-space: nowrap;
  }
  .requirements li {
    height: 42.7px;
    line-height: 42.7px;
  }
</style>
</head>
<body>
<main class="flyer">
  <svg class="backdrop-photo" viewBox="0 0 800 1200" role="img" aria-label="Photo of a desert road at sunset under a cloudy sky">
    <defs>
      <linearGradient id="skyToRoad" x1="0" y1="0" x2="0" y2="1">
        <stop offset="0" stop-color="#8fa4a4"/>
        <stop offset="0.35" stop-color="#d3bd7c"/>
        <stop offset="0.58" stop-color="#e39a32"/>
        <stop offset="0.66" stop-color="#9c7a55"/>
        <stop offset="1" stop-color="#7a6650"/>
      </linearGradient>
    </defs>
    <rect width="800" height="1200" fill="url(#skyToRoad)"/>
  </svg>

  <svg class="vehicle-photo" viewBox="0 0 616 292" role="img" aria-label="Photo of an orange and black three-wheeled open roadster">
    <rect width="616" height="292" rx="24" fill="var(--vehicle-tone)"/>
  </svg>

  <h1 class="title">REQUIREMENTS</h1>

  <ul class="highlights">
    <li>- Perfect for Birthdays and Anniversaries</li>
    <li>- Rentals available hourly, daily, and weekly</li>
    <li>- Group Rentals available at discounted rates</li>
    <li>- Enter to win a free rental - url and QR code</li>
  </ul>

  <svg class="bottom-band" viewBox="0 0 800 300" aria-hidden="true">
    <polygon points="0,150 800,5 800,300 0,300" fill="var(--band-black)"/>
    <polygon points="0,172 800,32 800,300 0,300" fill="var(--band-red)"/>
  </svg>

  <ul class="requirements">
    <li>At least 25 years of age</li>
    <li>Valid Driver's License</li>
    <li>Debit or Credit Card</li>
    <li>Must know how to drive a manual transmission or stick shift</li>
  </ul>
</main>
</body>
</html>
```